International Luxury Furniture and Accessories Outsourcing Company

We Need a Business Card design for a new Outsourcing company doing Business Internationally in the Luxury Furniture and Accessories Space. The company's name is GARETH VELLOR and we deal with clients in the high end and Luxury Space for Furniture and Accessories in the world. We would like Designs that speaks Luxury and Professionalism.

We like the Combination of the color Brown and Gold or Black and Gold. We are also open to other color combo.

We like some of the design of file attached.
Updates

This is Marcus and We really appreciate all of you taking the time out and putting the effort to help us jump start our new company. We have 2-3 designs that we like and will decide soon to pick one. Once again, Thank you to all of you !! Best Regards, Marcus

Industry/Entity Type

Business

```html
<!DOCTYPE html>
<html lang="en">
<head>
<meta charset="UTF-8">
<title>Gareth Vellor – Business Card</title>
<link href="https://fonts.googleapis.com/css2?family=Arimo:wght@700&family=Francois+One&display=swap" rel="stylesheet">
<style>
  :root {
    --brown: #3c2416;
    --paper: #ffffff;
  }
  html, body {
    margin: 0;
    padding: 0;
    width: 1200px;
    height: 309px;
    overflow: hidden;
    background: var(--paper);
  }
  .card-sheet {
    display: block;
    width: 1200px;
    height: 309px;
  }
  .fill-brown { fill: var(--brown); }
  .fill-paper { fill: var(--paper); }
  .name {
    font-family: "Arimo", Arial, sans-serif;
    font-weight: 700;
    letter-spacing: 0.5px;
  }
  .name--front { fill: var(--paper); font-size: 18px; }
  .name--mark { fill: var(--brown); font-size: 15px; }
  .name--back { fill: var(--paper); font-size: 20px; }
  .tagline {
    font-family: "Francois One", "Arial Narrow", sans-serif;
    font-size: 18px;
    fill: var(--brown);
  }
</style>
</head>
<body>
<svg class="card-sheet" viewBox="0 0 1440 375" preserveAspectRatio="none" xmlns="http://www.w3.org/2000/svg">
  <!-- Front of card -->
  <g class="card-front">
    <rect class="fill-brown" x="0" y="0" width="600" height="375"/>
    <rect class="fill-paper" x="116" y="0" width="164" height="255"/>
    <g class="brand-mark">
      <rect class="fill-brown" x="189" y="122" width="20" height="20"/>
      <text class="name name--mark" x="198" y="170" text-anchor="middle">GARETH VELLOR</text>
    </g>
    <text class="name name--front" x="197" y="269" text-anchor="middle">GARETH VELLOR</text>
  </g>

  <!-- Back of card -->
  <g class="card-back">
    <rect class="fill-brown" x="854" y="0" width="224" height="375"/>
    <rect class="fill-brown" x="1078" y="104" width="103" height="103"/>
    <rect class="fill-paper" x="986" y="207" width="92" height="93"/>
    <text class="name name--back" x="1093" y="160" text-anchor="middle">GARETH VELLOR</text>
    <text class="tagline" x="986" y="270" textLength="409" lengthAdjust="spacingAndGlyphs">LUXURY FURNITURE &amp; ACCESSORIES SPACE</text>
  </g>
</svg>
</body>
</html>
```